Business Card Design for Vantor Gear

We want to have a business card design for our company.
Company website: www.vantorgear-example.com.au
We looking for something cool, funky, and impressive, yet elegant.
Below are the contents that should be displayed on the card:
Front:
Name: Mark Dellow
Title: Sales & Purchasing
Company Name: Vantor Gear Pty Ltd
Phone: 02 5550 1473
Mobile: 0400 555 019
Email: mark@vantorgear-example.com.au
Website: www.vantorgear-example.com.au
Address: 17 Brackley St
Kestwood, NSW 2999
Back:
We buy sell new used Norvex and network equipment
• Huge Savings - save up to 95% off list prices
• Highest Reliability
• Comprehensive Warranty
• Fast delivery
• Large range of hardware in stock
Our logo can be downloaded at: www.vantorgear-example.com.au/logo.zip

```html
<!DOCTYPE html>
<html lang="en">
<head>
<meta charset="utf-8">
<title>Vantor Gear – Business Card</title>
<link rel="stylesheet" href="https://fonts.googleapis.com/css2?family=Cabin:wght@700&family=Exo+2:wght@700&family=Tinos&display=swap">
<style>
  :root {
    --bg: #000000;
    --brand-blue: #1b80d2;
    --text-blue: #1a8ad6;
    --tagline-grey: #b9b9b9;
    --mark-orange: #e8461f;
    --mark-faint: rgba(150, 40, 20, 0.22);
    --disc-shadow: rgba(255, 255, 255, 0.35);
  }
  html, body {
    margin: 0;
    padding: 0;
    width: 1200px;
    height: 686px;
    overflow: hidden;
    background: var(--bg);
  }
  .card {
    position: relative;
    width: 1200px;
    height: 686px;
    background: var(--bg);
    overflow: hidden;
    font-family: "Tinos", "Times New Roman", serif;
    color: var(--text-blue);
  }
  .backdrop-circle {
    position: absolute;
    left: 70px;
    top: 20px;
    width: 820px;
    height: 820px;
    border-radius: 50%;
    background: var(--mark-faint);
  }
  .brand-dot {
    position: absolute;
    left: 38px;
    top: 40px;
    width: 262px;
    height: 262px;
    border-radius: 50%;
    background: var(--mark-orange);
  }
  .brand-dot-shadow {
    position: absolute;
    left: 92px;
    top: 340px;
    width: 196px;
    height: 18px;
    border-radius: 50%;
    background: radial-gradient(ellipse at center, var(--disc-shadow), transparent 70%);
  }
  .brand-name {
    position: absolute;
    left: 444px;
    top: 66px;
    margin: 0;
    font-family: "Cabin", "Trebuchet MS", sans-serif;
    font-weight: 700;
    font-size: 140px;
    line-height: 1;
    color: var(--brand-blue);
    white-space: nowrap;
  }
  .brand-tagline {
    position: absolute;
    left: 448px;
    top: 258px;
    margin: 0;
    font-family: "Exo 2", "Arial", sans-serif;
    font-weight: 700;
    font-size: 31px;
    line-height: 1;
    letter-spacing: 0.5em;
    color: var(--tagline-grey);
    white-space: nowrap;
  }
  .contact-list {
    position: absolute;
    left: 44px;
    top: 410px;
    margin: 0;
    padding: 0;
    list-style: none;
  }
  .contact-item {
    display: flex;
    align-items: center;
    height: 44px;
    font-size: 34px;
    line-height: 1;
    white-space: nowrap;
  }
  .contact-item--mobile { margin-top: -1px; }
  .contact-item--email { margin-top: 10px; }
  .contact-item--web { margin-top: 13px; }
  .contact-icon {
    width: 40px;
    height: 40px;
    margin-right: 27px;
    flex: none;
    fill: var(--text-blue);
  }
  .person {
    position: absolute;
    left: 560px;
    top: 400px;
    width: 600px;
    text-align: center;
  }
  .person-name {
    margin: 0;
    font-size: 78px;
    line-height: 1;
    font-weight: 400;
    text-transform: uppercase;
    white-space: nowrap;
  }
  .person-role {
    margin: 9px 0 0;
    font-size: 60px;
    line-height: 1;
    white-space: nowrap;
  }
  .address {
    position: absolute;
    left: 169px;
    top: 611px;
    margin: 0;
    font-size: 58px;
    line-height: 1;
    font-style: normal;
    white-space: pre;
  }
</style>
</head>
<body>
<main class="card">
  <div class="backdrop-circle" aria-hidden="true"></div>

  <div class="brand-dot" aria-hidden="true"></div>
  <div class="brand-dot-shadow" aria-hidden="true"></div>

  <h1 class="brand-name">Vantor Gear</h1>
  <p class="brand-tagline">NETWORKING EQUIPMENT</p>

  <ul class="contact-list">
    <li class="contact-item contact-item--phone">
      <svg class="contact-icon" viewBox="0 0 40 40" aria-hidden="true">
        <path d="M4 14c0-5 7-8 16-8s16 3 16 8v3h-8v-4c-2-1-5-1.5-8-1.5s-6 .5-8 1.5v4H4z"/>
        <path d="M9 20l5-5h12l5 5v12H9z"/>
      </svg>
      <span>02 5550 1473</span>
    </li>
    <li class="contact-item contact-item--mobile">
      <svg class="contact-icon" viewBox="0 0 40 40" aria-hidden="true">
        <rect x="12" y="2" width="16" height="36" rx="2"/>
        <rect x="15" y="7" width="10" height="10" fill="#000"/>
        <rect x="15" y="21" width="3" height="3" fill="#000"/>
        <rect x="22" y="21" width="3" height="3" fill="#000"/>
        <rect x="15" y="27" width="3" height="3" fill="#000"/>
        <rect x="22" y="27" width="3" height="3" fill="#000"/>
      </svg>
      <span>0400 555 019</span>
    </li>
    <li class="contact-item contact-item--email">
      <svg class="contact-icon" viewBox="0 0 40 40" aria-hidden="true">
        <text x="20" y="33" text-anchor="middle" font-family="Arial, sans-serif" font-weight="700" font-size="38">@</text>
      </svg>
      <span>mark@vantorgear-example.com.au</span>
    </li>
    <li class="contact-item contact-item--web">
      <svg class="contact-icon" viewBox="0 0 40 40" aria-hidden="true">
        <circle cx="20" cy="20" r="17"/>
        <path d="M10 12c4-2 7 0 8 3s-2 5-4 6-2 5-5 4-3-9 1-13zM22 9c4 0 8 3 9 7-3 0-5-2-7-1s0 5 3 7-1 7-4 8c1-4-3-6-2-10s-3-7 1-11z" fill="#000"/>
      </svg>
      <span>www.vantorgear-example.com.au</span>
    </li>
  </ul>

  <div class="person">
    <h2 class="person-name">Mark Dellow</h2>
    <p class="person-role">Sales &amp; Purchasing</p>
  </div>

  <address class="address">17 Brackley St   Kestwood,  NSW 2999</address>
</main>
</body>
</html>
```